Amber Quill Letterhead

I just need letterhead for my integrative psychiatry business. I'm going to use this to do mailings to other doctors, as well as send letters to patients. Thank you

Industry/Entity Type

Business

```html
<!DOCTYPE html>
<html lang="en">
<head>
<meta charset="utf-8">
<title>Amber Quill Letterhead</title>
<link rel="stylesheet" href="https://fonts.googleapis.com/css2?family=Open+Sans:wght@400;600;700&display=swap">
<style>
  :root {
    --backdrop: #e9e6e1;
    --paper: #ffffff;
    --ink: #2b2b2b;
    --leaf-green: #2f6b34;
    --accent-green: #3f8a45;
    --bark-brown: #6a3a1e;
    --watermark: #ecebe6;
    --signature-tone: #d9d6cf;
  }
  * { box-sizing: border-box; margin: 0; padding: 0; }
  html, body {
    width: 1200px; height: 1024px; overflow: hidden;
    background: var(--backdrop);
    font-family: "Open Sans", Arial, sans-serif;
  }
  .letterhead {
    position: absolute; left: 253px; top: 22px;
    width: 694px; height: 980px;
    background: var(--paper);
    box-shadow: 0 4px 18px rgba(0,0,0,0.18);
    overflow: hidden;
  }
  .brand {
    position: absolute; left: 44px; top: 30px;
    display: flex; align-items: center; gap: 10px;
  }
  .brand-dot { width: 34px; height: 34px; border-radius: 50%; background: var(--leaf-green); }
  .brand-name { font-size: 20px; font-weight: 600; color: var(--leaf-green); }
  .contact {
    position: absolute; right: 44px; top: 40px;
    padding-left: 22px;
    border-left: 1px solid #d5d5d5;
    font-size: 12px; line-height: 17px; color: var(--accent-green);
  }
  .watermark-area {
    position: absolute; left: 140px; top: 150px; width: 520px; height: 640px;
    background: radial-gradient(ellipse at 55% 35%, var(--watermark) 0%, rgba(236,235,230,0.55) 45%, rgba(255,255,255,0) 72%);
  }
  .letter-body {
    position: absolute; left: 60px; top: 132px; width: 500px;
    font-size: 12px; line-height: 16px; color: var(--ink);
  }
  .salutation { margin-bottom: 8px; }
  .salutation strong { font-weight: 700; }
  .letter-body p.paragraph { text-indent: 20px; margin-bottom: 12px; }
  .signature {
    position: absolute; left: 60px; top: 560px; width: 210px; height: 44px;
    background: linear-gradient(90deg, var(--signature-tone), rgba(217,214,207,0.3));
    border-radius: 4px;
  }
  .signer { position: absolute; left: 60px; top: 616px; }
  .signer-name { font-size: 19px; color: var(--ink); }
  .signer-name strong { font-weight: 600; }
  .credential { font-size: 12.5px; font-weight: 700; color: var(--accent-green); line-height: 17px; }
  .footer-band { position: absolute; left: 0; bottom: 0; width: 694px; height: 250px; }
  .address {
    position: absolute; left: 44px; bottom: 36px;
    font-size: 13px; color: #ffffff; letter-spacing: 0.3px;
  }
</style>
</head>
<body>
  <main class="letterhead">
    <div class="watermark-area" role="img" aria-label="Faint background decoration area"></div>

    <header class="brand">
      <span class="brand-dot"></span>
      <span class="brand-name">Amber Quill</span>
    </header>

    <address class="contact">
      555-014-2206<br>
      555-014-2207<br>
      www.amberquillcare.com
    </address>

    <section class="letter-body">
      <p class="salutation">Lorem<br><strong>ipsum dolor sit amet,</strong></p>
      <p class="paragraph">consectetur adipiscing elit. Duis facilisis elementum dui, bibendum pulvinar nulla malesuada quis. Curabitur ut leo quam. Pellentesque laoreet metus risus, non fermentum arcu malesuada vitae. Vestibulum dui libero, vestibulum non quam sit amet, auctor lobortis tortor. Integer blandit enim vitae adipiscing adipiscing. Vivamus metus lacus, porta at aliquam sit amet.</p>
      <p class="paragraph">pretium ut eros. Curabitur a dui interdum, elementum urna ut, venenatis erat. Fusce feugiat odio sed dui rhoncus auctor. Aenean posuere, odio ut facilisis tempus, nunc mauris convallis lacus, eget vulputate enim purus ac odio. Donec blandit et ipsum a aliquet. Mauris semper diam in velit vestibulum, sit amet molestie purus convallis. Duis pulvinar porttitor magna in malesuada.</p>
      <p class="paragraph">Nullam auctor neque orci, nec ornare odio auctor et. Phasellus eu sapien nec nibh lobortis commodo. Donec nec commodo nibh. Sed nec nulla et magna fermentum suscipit. Nam ligula nunc, facilisis iaculis venenatis eget,</p>
      <p class="paragraph">gravida consectetur odio. Donec in leo ac felis vestibulum feugiat. In at orci id justo adipiscing vehicula. Sed tortor purus, pellentesque vel lobortis nec, tincidunt vitae mi. Duis pellentesque augue vitae pharetra euismod.</p>
      <p class="paragraph">Duis vulputate, libero nec vehicula pretium, mi nisi tristique mauris, ac porttitor diam metus at ante. Pellentesque magna arcu, viverra ac lacinia nec, pharetra id est. Maecenas ullamcorper mattis tellus, et dapibus arcu sagittis malesuada.</p>
    </section>

    <div class="signature" role="img" aria-label="Handwritten signature"></div>

    <div class="signer">
      <p class="signer-name">Corinne <strong>Halvorsen</strong>, MD</p>
      <p class="credential">Diplomate, Coastal Board of Psychiatry and Neurology</p>
      <p class="credential">Diplomate, Coastal Board of Integrative and Holistic Medicine</p>
    </div>

    <svg class="footer-band" viewBox="0 0 694 250" aria-hidden="true">
      <path d="M0,70 C150,60 260,150 420,185 C520,205 610,195 694,180 L694,250 L0,250 Z" fill="var(--leaf-green)"/>
      <path d="M20,62 C120,20 210,70 300,140" fill="none" stroke="var(--bark-brown)" stroke-width="4" stroke-linecap="round"/>
      <path d="M440,176 C540,168 620,180 694,175" fill="none" stroke="var(--bark-brown)" stroke-width="5" stroke-linecap="round"/>
    </svg>

    <p class="address">2170 Birchwood Lane, Suite 310, Maple Hollow, CA 95012</p>
  </main>
</body>
</html>
```